Ember Evening - A5 double sided pamphlet/brochure

We need a 1 page, double sided brochure made for a new themed night at our club…Ember Evening.

Our club is Velvet Lounge 7. However, this brochure is to have nothing sexual about it.

The theme is to be "Tradies"... Tradesman - painters, builders etc

We want it to be fairly simple. Very easy to read and to the point.

I have attached our logo - MUST BE ON THE BROCHURE

I have also attached a rough draft of the look. But it is very basic. We want something that looks much better than this! You DO NOT need to follow this layout.

This is to be a 1 Page, double sided, size: A5

It is to have the following information:

Title: Ember Evening
Kicks off June 2nd
Bar snacks
Front door prices
Maple Bar access 3-9pm
Entry to main showroom after 9pm (dress code applies)

Lucky Draw every hour
Win: VIP Memberships, Entertainment vouchers and more!

Small text:
83 Larkwood St, Melbourne
9517 3302
www.velvetlounge7.com.au

Very small text:
Sexually explicit material may offend
18+ only

Target Market(s)

young men, in the tradesman field of work, men who drink/go out/hang with their mates.

Industry/Entity Type

Club

Requirements
Must have
• Must have our logo
Nice to have
• The tradesman theme means it is masculine and for workers.

So anything with hazzard tape, road signs, machinery etc (but still general enough for all fields of work)

We are a (strip) club. So something conservative but maybe beer, or a bit of a nightclub look to the front page will be fine.

The main thing is to keep it simple and easy to read.
Should not have
• Nothing sexual.

There are still some women in trade work, and we don't want to offend.

```html
<!DOCTYPE html>
<html lang="en">
<head>
<meta charset="utf-8">
<title>Ember Evening – Velvet Lounge 7</title>
<link rel="stylesheet" href="https://fonts.googleapis.com/css2?family=Anton&family=Archivo+Black&family=Lobster&family=Oswald:wght@500;700&display=swap">
<style>
  :root {
    --page: #ffffff;
    --ink: #101010;
    --panel-top: #2b2b2b;
    --panel-bottom: #0c0c0c;
    --band: #050505;
    --tear: #d9d9d9;
    --white: #ffffff;
    --grey: #9a9a9a;
    --red: #e3141b;
    --gold-light: #f4e3a6;
    --gold-dark: #b08a3a;
    --scene-a: #2a2f4a;
    --scene-b: #5b3b5e;
    --scene-c: #15161f;
  }
  * { box-sizing: border-box; margin: 0; padding: 0; }
  html, body { width: 1200px; height: 843px; overflow: hidden; background: var(--page); }
  .spread { position: relative; width: 1200px; height: 843px; }

  .side {
    position: absolute; top: 0; height: 843px; overflow: hidden;
    background: linear-gradient(160deg, var(--panel-top), var(--panel-bottom) 70%);
    color: var(--white);
  }
  .side--back { left: 0; width: 585px; }
  .side--front { left: 598px; width: 602px; }

  .brand {
    position: absolute; display: flex; align-items: center; gap: 10px;
    font-family: "Anton", sans-serif; color: var(--white); line-height: 0.95;
    text-transform: uppercase; text-align: center;
  }
  .brand__dot { flex: none; border-radius: 50%; background: var(--red); }
  .side--back .brand { left: 45px; top: 62px; font-size: 40px; }
  .side--back .brand__dot { width: 34px; height: 34px; }
  .side--front .brand { left: 95px; top: 135px; font-size: 76px; }
  .side--front .brand__dot { width: 60px; height: 60px; }

  .launch-tag {
    position: absolute; left: 355px; top: 28px; width: 86px; height: 80px;
    background: linear-gradient(135deg, #f2f2f2, #9c9c9c);
  }
  .launch-date {
    position: absolute; left: 455px; top: 44px; width: 80px;
    font-family: "Oswald", sans-serif; font-weight: 700; font-size: 17px;
    line-height: 1.05; text-align: center; text-transform: uppercase;
  }

  .band {
    position: absolute; background: var(--band);
    border-top: 6px solid var(--tear); border-bottom: 5px solid var(--tear);
    transform: rotate(-3deg);
    box-shadow: 0 6px 14px rgba(0,0,0,.6);
  }
  .side--back .band { left: -30px; top: 165px; width: 650px; height: 245px; }
  .side--front .band { left: -30px; top: 430px; width: 670px; height: 265px; }

  .event-title {
    position: absolute; font-family: "Anton", sans-serif; text-transform: uppercase;
    color: var(--white); -webkit-text-stroke: 3px var(--ink);
    text-shadow: 4px 4px 0 #555; letter-spacing: 1px; white-space: nowrap;
    line-height: 1;
    transform: rotate(-6deg) scaleY(1.25); transform-origin: left bottom;
  }
  .side--back .event-title { left: 38px; top: 205px; font-size: 80px; }
  .side--front .event-title { left: 42px; top: 478px; font-size: 84px; }

  .event-details {
    position: absolute; font-family: "Oswald", sans-serif; font-weight: 700;
    transform: rotate(-3deg); transform-origin: left top; text-align: center;
  }
  .event-details__entry { font-size: 15px; }
  .event-details__entry span { color: var(--grey); font-weight: 500; }
  .event-details__bar { font-size: 24px; letter-spacing: 1px; }
  .side--back .event-details { left: 132px; top: 342px; }
  .side--front .event-details { left: 150px; top: 618px; }

  .lucky-draw {
    position: absolute; left: 310px; top: 385px; width: 260px; height: 100px;
    font-family: "Lobster", cursive; color: var(--red);
    -webkit-text-stroke: 1px var(--white);
  }
  .lucky-draw__word { position: absolute; font-size: 34px; }
  .lucky-draw__word--a { left: 0; top: 5px; transform: rotate(-18deg); }
  .lucky-draw__word--b { left: 170px; top: 5px; transform: rotate(18deg); }
  .lucky-draw__word--c { left: 60px; top: 48px; font-size: 30px; transform: rotate(-10deg); }
  .lucky-draw__mugs {
    position: absolute; left: 92px; top: 4px; width: 70px; height: 52px;
    border-radius: 8px; background: linear-gradient(180deg, #fff7e0 25%, #e99a21 35%, #b8660f);
  }

  .prizes {
    position: absolute; left: 38px; top: 470px; text-transform: uppercase;
    font-family: "Archivo Black", sans-serif;
    background: linear-gradient(180deg, var(--gold-light), var(--gold-dark));
    -webkit-background-clip: text; background-clip: text; color: transparent;
  }
  .prizes__lead { margin-left: 57px; font-size: 36px; letter-spacing: 5px; line-height: 1.2; }
  .prizes__main { font-size: 36px; line-height: 1.25; }
  .prizes__main b { font-size: 44px; font-weight: 400; }
  .prizes__more { font-size: 23px; line-height: 1.5; }
  .prizes__more span { text-transform: none; }

  .perks {
    position: absolute; font-family: "Oswald", sans-serif; font-weight: 700;
    text-transform: uppercase; transform: skewX(-10deg); white-space: nowrap;
  }
  .perks--snacks { left: 92px; top: 628px; font-size: 38px; }
  .perks--live { left: 242px; top: 668px; font-size: 34px; color: var(--red); }
  .perks--price { left: 38px; top: 712px; font-size: 40px; }

  .contact {
    position: absolute; left: 0; right: 0; top: 790px; text-align: center;
    font-family: "Oswald", sans-serif; font-weight: 700; font-size: 15px;
    text-transform: uppercase; word-spacing: 2px;
  }
  .contact__sep { margin: 0 8px; }

  .scene {
    position: absolute; inset: 0;
    background: radial-gradient(ellipse at 70% 35%, var(--scene-b), transparent 55%),
                linear-gradient(180deg, var(--scene-a), var(--scene-c) 85%);
  }
  .notice {
    position: absolute; left: 0; right: 0; top: 766px; text-align: center;
    font-family: "Oswald", sans-serif; font-weight: 500; font-size: 9px;
    color: var(--grey); text-transform: uppercase; letter-spacing: 1px;
  }
</style>
</head>
<body>
<main class="spread">

  <section class="side side--back">
    <div class="brand"><span class="brand__dot"></span><span>Velvet<br>Lounge 7</span></div>
    <div class="launch-tag" role="img" aria-label="Curled paper sticker"></div>
    <p class="launch-date">Kicks off June 2<sup>nd</sup></p>

    <div class="band"></div>
    <h1 class="event-title">Ember Evening</h1>
    <div class="event-details">
      <p class="event-details__entry">Entry to main showroom after 9pm <span>(dress code applies)</span></p>
      <p class="event-details__bar">Maple Bar access 3-9 pm</p>
    </div>

    <div class="lucky-draw">
      <span class="lucky-draw__word lucky-draw__word--a">Lucky</span>
      <div class="lucky-draw__mugs" role="img" aria-label="Two clinking beer mugs"></div>
      <span class="lucky-draw__word lucky-draw__word--b">Draw</span>
      <span class="lucky-draw__word lucky-draw__word--c">every hour</span>
    </div>

    <div class="prizes">
      <p class="prizes__lead">Win...</p>
      <p class="prizes__main"><b>VIP</b> Memberships,</p>
      <p class="prizes__more">Entertainment Vouchers <span>and more!</span></p>
    </div>

    <p class="perks perks--snacks">Bar Snacks</p>
    <p class="perks perks--live">Live Entertainment</p>
    <p class="perks perks--price">Front Door Prices</p>

    <p class="contact">83 Larkwood St, Melbourne<span class="contact__sep">•</span>9517 3302<span class="contact__sep">•</span>www.velvetlounge7.com.au</p>
  </section>

  <section class="side side--front">
    <div class="scene" role="img" aria-label="Night-time city laneway with a lit bar entrance and red carpet"></div>
    <div class="brand"><span class="brand__dot"></span><span>Velvet<br>Lounge 7</span></div>

    <div class="band"></div>
    <h2 class="event-title">Ember Evening</h2>
    <div class="event-details">
      <p class="event-details__entry">Entry to main showroom after 9pm <span>(dress code applies)</span></p>
      <p class="event-details__bar">Maple Bar access 3-9 pm</p>
    </div>

    <p class="notice">Sexually explicit material may offend &nbsp;|&nbsp; 18+ only</p>
    <p class="contact">83 Larkwood St, Melbourne<span class="contact__sep">•</span>9517 3302<span class="contact__sep">•</span>www.velvetlounge7.com.au</p>
  </section>

</main>
</body>
</html>
```